Mexican Tacos Food Truck Menu

Attached is the food truck logo. Need a menu to be place next to the window. Must contain:
- logo in the header (left or centered)
- Grouping elements: Dessert, drinks, Apps, etc.
- Group elements.
- main descrition (these are examples) Spaguetti, Pastor, etc
- Notes. Under main item for ingrediens, GF, dairy, etc.
- Price. Should be fairly visible and justify to the right
No prodiving target size but the I the design should accomodate at least two Group columns. I should be able to add or remove as needed.
Since the food truck is blue I think menu should be white based unless you have other options. I will update blue code

```html
<!DOCTYPE html>
<html lang="en">
<head>
<meta charset="utf-8">
<title>Taco Plaza – Food Truck Menu</title>
<link rel="stylesheet" href="https://fonts.googleapis.com/css2?family=Caveat+Brush&family=Montserrat:wght@400;600;700&display=swap">
<style>
  :root {
    --page-bg: #f1f1f1;
    --paper: #ffffff;
    --frame: #e59442;
    --frame-deep: #b8322a;
    --ribbon: #f4cf37;
    --ribbon-fold: #c9a21d;
    --red: #e8423a;
    --ink: #1d1d1d;
    --ink-soft: #3a3a3a;
    --rule: #bdbdbd;
    --sketch: #d9d9d9;
  }
  * { box-sizing: border-box; margin: 0; padding: 0; }
  html, body { width: 1200px; height: 4000px; overflow: hidden; background: var(--page-bg); }
  body { position: relative; font-family: "Montserrat", Arial, sans-serif; color: var(--ink); }

  .menu { position: absolute; left: 50px; top: 780px; width: 1100px; height: 2440px; box-shadow: 0 10px 30px rgba(0,0,0,.18); }
  .menu-frame { position: absolute; inset: 0; background: linear-gradient(135deg, var(--frame), var(--frame-deep) 50%, var(--frame)); }
  .menu-sheet { position: absolute; inset: 24px; background: var(--paper); }

  .sketch { position: absolute; background: radial-gradient(ellipse at center, #eeeeee 0%, var(--sketch) 70%, transparent 72%); }

  .brand { position: absolute; left: 440px; top: 110px; width: 220px; text-align: center; }
  .brand-dot { width: 70px; height: 70px; border-radius: 50%; background: var(--ribbon); margin: 0 auto 14px; }
  .brand-name { font-weight: 700; font-size: 34px; color: var(--red); line-height: 1; }

  .banner { position: absolute; width: 360px; height: 110px; }
  .banner svg { position: absolute; inset: 0; }
  .banner-title { position: absolute; left: 0; right: 0; top: 16px; text-align: center; font-family: "Caveat Brush", cursive; font-weight: 400; font-size: 50px; line-height: 1; color: var(--ink); }

  .item { position: absolute; }
  .item-row { display: flex; align-items: baseline; gap: 10px; }
  .item-name { font-weight: 700; font-size: 18px; color: var(--red); white-space: nowrap; }
  .item-rule { flex: 1; border-bottom: 1.5px solid var(--rule); transform: translateY(-4px); }
  .item-price { font-weight: 700; font-size: 18px; color: var(--red); white-space: nowrap; }
  .item-note { font-size: 13px; line-height: 1.3; color: var(--ink-soft); width: 400px; margin-top: 6px; }

  .zigzag { position: absolute; height: 24px; background: linear-gradient(90deg, #f1c232, #e8423a 35%, #3aa17e 70%, #f1c232); opacity: .85; }

  .tag-box { position: absolute; background: var(--red); color: #fff; text-align: center; font-weight: 700; font-size: 20px; line-height: 1.6; display: flex; align-items: center; justify-content: center; border-radius: 4px; }

  .drinks-box { position: absolute; left: 75px; top: 1156px; width: 470px; height: 147px; }
  .drinks-box svg { position: absolute; inset: 0; }

  .note-text { position: absolute; left: 60px; top: 1335px; width: 460px; font-size: 14px; line-height: 1.3; color: var(--ink); }
  .note-text p + p { margin-top: 12px; }
  .note-text p.narrow { width: 310px; }

  .gf-box { position: absolute; left: 564px; top: 912px; width: 470px; height: 146px; background: var(--red); border-radius: 4px; }
  .gf-box .banner-title { color: #fff; top: 12px; }
  .gf-box .item-name, .gf-box .item-price, .gf-box .item-note { color: #fff; }
  .gf-box .item-rule { border-color: rgba(255,255,255,.6); }
</style>
</head>
<body>
<main class="menu">
  <div class="menu-frame" role="img" aria-label="Colourful Mexican zigzag border pattern"></div>
  <div class="menu-sheet"></div>

  <div class="sketch" style="left:66px;top:85px;width:340px;height:225px" role="img" aria-label="Line drawing of nachos with dip, a taco and a burrito"></div>
  <div class="sketch" style="left:667px;top:103px;width:330px;height:175px" role="img" aria-label="Line drawing of a cake and wedges of cheese"></div>

  <div class="brand">
    <div class="brand-dot"></div>
    <div class="brand-name">Taco Plaza</div>
  </div>

  <!-- Left column -->
  <div class="banner" style="left:113px;top:295px">
    <svg viewBox="0 0 360 110" width="360" height="110" aria-hidden="true">
      <polygon points="0,100 30,80 8,62 60,58 60,96" fill="var(--ribbon)"/>
      <polygon points="360,100 330,80 352,62 300,58 300,96" fill="var(--ribbon)"/>
      <polygon points="40,78 60,96 60,78" fill="var(--ribbon-fold)"/>
      <polygon points="320,78 300,96 300,78" fill="var(--ribbon-fold)"/>
      <path d="M40,12 Q180,0 320,12 L320,80 Q180,68 40,80 Z" fill="var(--ribbon)"/>
    </svg>
    <h2 class="banner-title">Dessert</h2>
  </div>

  <div class="item" style="left:70px;top:429px;width:460px">
    <div class="item-row"><span class="item-name">Lorem Ipsum</span><span class="item-rule"></span><span class="item-price">$ 10.90</span></div>
    <p class="item-note">Lorem Ipsum has been the industry's standard dummy text ever since</p>
  </div>
  <div class="item" style="left:70px;top:509px;width:460px">
    <div class="item-row"><span class="item-name">Lorem Ipsum</span><span class="item-rule"></span><span class="item-price">$ 10.90</span></div>
    <p class="item-note">Lorem Ipsum has been the industry's standard dummy text ever since</p>
  </div>
  <div class="item" style="left:70px;top:590px;width:460px">
    <div class="item-row"><span class="item-name">Lorem Ipsum</span><span class="item-rule"></span><span class="item-price">$ 10.90</span></div>
    <p class="item-note">Lorem Ipsum has been the industry's standard dummy text ever since</p>
  </div>

  <div class="zigzag" style="left:75px;top:677px;width:433px" role="img" aria-label="Zigzag divider pattern"></div>

  <div class="tag-box" style="left:113px;top:714px;width:353px;height:94px">VEGGIE / CHICKEN / STEAK<br>BBQ / PASTOR</div>

  <div class="banner" style="left:110px;top:830px">
    <svg viewBox="0 0 360 110" width="360" height="110" aria-hidden="true">
      <polygon points="0,100 30,80 8,62 60,58 60,96" fill="var(--ribbon)"/>
      <polygon points="360,100 330,80 352,62 300,58 300,96" fill="var(--ribbon)"/>
      <polygon points="40,78 60,96 60,78" fill="var(--ribbon-fold)"/>
      <polygon points="320,78 300,96 300,78" fill="var(--ribbon-fold)"/>
      <path d="M40,12 Q180,0 320,12 L320,80 Q180,68 40,80 Z" fill="var(--ribbon)"/>
    </svg>
    <h2 class="banner-title">Apps</h2>
  </div>

  <div class="item" style="left:60px;top:955px;width:460px">
    <div class="item-row"><span class="item-name">Lorem Ipsum</span><span class="item-rule"></span><span class="item-price">$ 10.90</span></div>
    <p class="item-note">Lorem Ipsum has been the industry's standard dummy text ever since</p>
  </div>

  <div class="banner" style="left:110px;top:1036px">
    <svg viewBox="0 0 360 110" width="360" height="110" aria-hidden="true">
      <polygon points="0,100 30,80 8,62 60,58 60,96" fill="var(--ribbon)"/>
      <polygon points="360,100 330,80 352,62 300,58 300,96" fill="var(--ribbon)"/>
      <polygon points="40,78 60,96 60,78" fill="var(--ribbon-fold)"/>
      <polygon points="320,78 300,96 300,78" fill="var(--ribbon-fold)"/>
      <path d="M40,12 Q180,0 320,12 L320,80 Q180,68 40,80 Z" fill="var(--ribbon)"/>
    </svg>
    <h2 class="banner-title">Drinks</h2>
  </div>

  <div class="drinks-box">
    <svg viewBox="0 0 470 147" width="470" height="147" aria-hidden="true">
      <polygon points="16,2 454,2 468,16 468,131 454,145 16,145 2,131 2,16" fill="none" stroke="var(--ink)" stroke-width="3"/>
    </svg>
  </div>
  <div class="item" style="left:95px;top:1190px;width:430px">
    <div class="item-row"><span class="item-name">Lorem Ipsum</span><span class="item-rule"></span><span class="item-price">$ 10.90</span></div>
  </div>
  <div class="item" style="left:95px;top:1222px;width:430px">
    <div class="item-row"><span class="item-name">Lorem Ipsum</span><span class="item-rule"></span><span class="item-price">$ 10.90</span></div>
  </div>
  <div class="item" style="left:95px;top:1256px;width:430px">
    <div class="item-row"><span class="item-name">Lorem Ipsum</span><span class="item-rule"></span><span class="item-price">$ 10.90</span></div>
  </div>

  <div class="note-text">
    <p>There are many variations of passages of Lorem Ipsum available, but the majority have suffered alteration in some form, by injected humour</p>
    <p class="narrow">There are many variations of passages of Lorem Ipsum available, but the majority have suffered alteration in some form, by injected humour</p>
  </div>
  <div class="sketch" style="left:395px;top:1372px;width:131px;height:94px" role="img" aria-label="Small line drawing of a plated dish"></div>

  <!-- Right column -->
  <div class="banner" style="left:627px;top:295px">
    <svg viewBox="0 0 360 110" width="360" height="110" aria-hidden="true">
      <polygon points="0,100 30,80 8,62 60,58 60,96" fill="var(--ribbon)"/>
      <polygon points="360,100 330,80 352,62 300,58 300,96" fill="var(--ribbon)"/>
      <polygon points="40,78 60,96 60,78" fill="var(--ribbon-fold)"/>
      <polygon points="320,78 300,96 300,78" fill="var(--ribbon-fold)"/>
      <path d="M40,12 Q180,0 320,12 L320,80 Q180,68 40,80 Z" fill="var(--ribbon)"/>
    </svg>
    <h2 class="banner-title">Spaguetti</h2>
  </div>

  <div class="item" style="left:573px;top:429px;width:461px">
    <div class="item-row"><span class="item-name">Lorem Ipsum</span><span class="item-rule"></span><span class="item-price">$ 10.90</span></div>
    <p class="item-note">Lorem Ipsum has been the industry's standard dummy text ever since</p>
  </div>
  <div class="item" style="left:573px;top:509px;width:461px">
    <div class="item-row"><span class="item-name">Lorem Ipsum</span><span class="item-rule"></span><span class="item-price">$ 10.90</span></div>
    <p class="item-note">Lorem Ipsum has been the industry's standard dummy text ever since</p>
  </div>

  <div class="banner" style="left:627px;top:570px">
    <svg viewBox="0 0 360 110" width="360" height="110" aria-hidden="true">
      <polygon points="0,100 30,80 8,62 60,58 60,96" fill="var(--ribbon)"/>
      <polygon points="360,100 330,80 352,62 300,58 300,96" fill="var(--ribbon)"/>
      <polygon points="40,78 60,96 60,78" fill="var(--ribbon-fold)"/>
      <polygon points="320,78 300,96 300,78" fill="var(--ribbon-fold)"/>
      <path d="M40,12 Q180,0 320,12 L320,80 Q180,68 40,80 Z" fill="var(--ribbon)"/>
    </svg>
    <h2 class="banner-title">Pastor</h2>
  </div>

  <div class="item" style="left:573px;top:709px;width:461px">
    <div class="item-row"><span class="item-name">Lorem Ipsum</span><span class="item-rule"></span><span class="item-price">$ 10.90</span></div>
    <p class="item-note">Lorem Ipsum has been the industry's standard dummy text ever since</p>
  </div>
  <div class="item" style="left:573px;top:780px;width:461px">
    <div class="item-row"><span class="item-name">Lorem Ipsum</span><span class="item-rule"></span><span class="item-price">$ 10.90</span></div>
    <p class="item-note">Lorem Ipsum has been the industry's standard dummy text ever since</p>
  </div>

  <div class="zigzag" style="left:573px;top:866px;width:433px" role="img" aria-label="Zigzag divider pattern"></div>

  <div class="gf-box">
    <h2 class="banner-title">Gluten Free</h2>
    <div class="item" style="left:12px;top:76px;width:446px">
      <div class="item-row"><span class="item-name">Lorem Ipsum</span><span class="item-rule"></span><span class="item-price">$ 10.90</span></div>
      <p class="item-note">Lorem Ipsum has been the industry's standard dummy text ever since</p>
    </div>
  </div>

  <div class="banner" style="left:615px;top:1098px">
    <svg viewBox="0 0 360 110" width="360" height="110" aria-hidden="true">
      <polygon points="0,100 30,80 8,62 60,58 60,96" fill="var(--ribbon)"/>
      <polygon points="360,100 330,80 352,62 300,58 300,96" fill="var(--ribbon)"/>
      <polygon points="40,78 60,96 60,78" fill="var(--ribbon-fold)"/>
      <polygon points="320,78 300,96 300,78" fill="var(--ribbon-fold)"/>
      <path d="M40,12 Q180,0 320,12 L320,80 Q180,68 40,80 Z" fill="var(--ribbon)"/>
    </svg>
    <h2 class="banner-title">Ingrediens</h2>
  </div>

  <div class="item" style="left:564px;top:1228px;width:470px">
    <div class="item-row"><span class="item-name">Lorem Ipsum</span><span class="item-rule"></span><span class="item-price">$ 10.90</span></div>
    <p class="item-note">Lorem Ipsum has been the industry's standard dummy text ever since</p>
  </div>

  <div class="banner" style="left:615px;top:1292px">
    <svg viewBox="0 0 360 110" width="360" height="110" aria-hidden="true">
      <polygon points="0,100 30,80 8,62 60,58 60,96" fill="var(--ribbon)"/>
      <polygon points="360,100 330,80 352,62 300,58 300,96" fill="var(--ribbon)"/>
      <polygon points="40,78 60,96 60,78" fill="var(--ribbon-fold)"/>
      <polygon points="320,78 300,96 300,78" fill="var(--ribbon-fold)"/>
      <path d="M40,12 Q180,0 320,12 L320,80 Q180,68 40,80 Z" fill="var(--ribbon)"/>
    </svg>
    <h2 class="banner-title">Dairy</h2>
  </div>

  <div class="item" style="left:564px;top:1423px;width:470px">
    <div class="item-row"><span class="item-name">Lorem Ipsum</span><span class="item-rule"></span><span class="item-price">$ 10.90</span></div>
    <p class="item-note">Lorem Ipsum has been the industry's standard dummy text ever since</p>
  </div>
</main>
</body>
</html>
```